Classic Minimalistic Business Card

Design a classic, minimalistic Business Card. Please find inspiration in the attached Classic Minimalistic examples. My information:
Name: Glen Ovamir
Company: Ovamir Capital
Logo: OC
Address: 1470 N Thornwick Rd, Suite 210 | Brenwick, IL 60999
Phone: 630-555-0192
Email: glenovamir@pvt.insure
Slogan: Building Strength Through Capital

Feel free to leave out any of the information above except my name.

I have selected Double-sided, but I am also open to Single-sided

Target Market(s)

22-70. income greater than 150k/year

Industry/Entity Type

Finance

Contact Information for Business Card

See Project Description

Requirements
Must have
• Ivory or "antiqued" background similar to the reference pictures

```html
<!DOCTYPE html>
<html lang="en">
<head>
<meta charset="utf-8">
<title>Ovamir Capital — Business Card</title>
<link href="https://fonts.googleapis.com/css2?family=Cinzel:wght@400;700&family=Pinyon+Script&display=swap" rel="stylesheet">
<style>
  :root {
    --page: #ffffff;
    --card: #f4d6a5;
    --ink: #2a2421;
  }
  html, body {
    margin: 0;
    padding: 0;
    width: 1200px;
    height: 1200px;
    overflow: hidden;
    background: var(--page);
  }
  .canvas {
    position: relative;
    width: 1200px;
    height: 1200px;
  }
  .card {
    position: absolute;
    left: 294px;
    width: 619px;
    height: 353px;
    background: var(--card);
    color: var(--ink);
  }
  .card--front { top: 203px; }
  .card--back  { top: 629px; }

  .monogram {
    position: absolute;
    left: 50%;
    top: 54px;
    width: 98px;
    height: 98px;
    margin-left: -49px;
  }
  .monogram text {
    font-family: "Cinzel", serif;
    font-weight: 400;
    fill: var(--ink);
  }

  .centered {
    position: absolute;
    left: 0;
    right: 0;
    text-align: center;
    margin: 0;
    white-space: nowrap;
  }
  .holder-name {
    top: 184px;
    font-family: "Cinzel", serif;
    font-weight: 700;
    font-size: 29px;
    letter-spacing: 0.5px;
  }
  .slogan {
    top: 262px;
    font-family: "Pinyon Script", cursive;
    font-size: 32px;
  }
  .company-name {
    top: 160px;
    font-family: "Cinzel", serif;
    font-weight: 700;
    font-size: 13px;
    letter-spacing: 1.6px;
  }
  .address {
    top: 281px;
    font-family: "Cinzel", serif;
    font-weight: 400;
    font-size: 15px;
    letter-spacing: 1px;
    text-transform: uppercase;
  }
  .phone {
    top: 306px;
    font-family: "Cinzel", serif;
    font-weight: 700;
    font-size: 22px;
    letter-spacing: 0.5px;
  }
</style>
</head>
<body>
<div class="canvas">

  <section class="card card--front">
    <svg class="monogram" viewBox="0 0 98 98" aria-label="OC">
      <circle cx="49" cy="49" r="46" fill="none" stroke="var(--ink)" stroke-width="3.5"/>
      <text x="49" y="60" text-anchor="middle" font-size="32">OC</text>
    </svg>
    <h1 class="centered holder-name">GLEN OVAMIR</h1>
    <p class="centered slogan">Building Strength Through Capital</p>
  </section>

  <section class="card card--back">
    <svg class="monogram" viewBox="0 0 98 98" aria-label="OC">
      <circle cx="49" cy="49" r="46" fill="none" stroke="var(--ink)" stroke-width="3.5"/>
      <text x="49" y="60" text-anchor="middle" font-size="32">OC</text>
    </svg>
    <p class="centered company-name">OVAMIR CAPITAL</p>
    <p class="centered address">1470 N Thornwick Rd, Suite 210 | Brenwick, IL 60999</p>
    <p class="centered phone">630-555-0192</p>
  </section>

</div>
</body>
</html>
```